Fast Money - Simple Book Cover Design

Hello,

I am in need of a cover for my new book. The Book Title Is

"Standing Growth - Keys to Glowing Customer Ratings That Fill The Calendar and Draw Fresh Clients Through Every Entrance!"

Author: Fireman Dale Orsworth

What I want: This is a book for businesses on improving their online reputation. I want to have 5 Stars on the cover. You can look at this quarvex search for ideas of what I am meaning.....

(copy and paste)

http://www.quarvex-find.example/search?q=5+star+online+reviews&mode=images&ref=kx7Lp2QwZt9 (copy and paste)

I am open to different color schemes for the book. I am partial to dark blues if you make it look good. Here is another book that I really like the cover of....

http://www.brindlemart.example/Clipwave-Tactics-Earning-Promotion-ebook/item/Z93KT4WQPX

I want the cover BOLD and to STAND OUT.

I am looking for a design to help establish me as an authority for online reputation marketing. This book will be both in Pagely format and be used in print as well.

I am open to questions....

Thanks!

Dale

Reason: I don't believe we have received the right designs. I am going to give everyone more time...

Reason: Hi everyone, I had some stuff come up and was not able to be involved in this project. I am extending because we have not seen the exact thing we want and need time to work with designers to get it right. Thanks Dale

Reason: I am currently traveling and can't wrap this up until I get back.

Target Market(s)

Business Owners

Industry/Entity Type

Business

Requirements
Must have
• Title and Subtitle

Author Name

5 Stars Images....
Nice to have
• Creativity

Bold and stand out

Professional

Should not have
• thin text, small to read text, lame graphics,

```html
<!DOCTYPE html>
<html lang="en">
<head>
<meta charset="utf-8">
<title>Standing Growth — Book Cover</title>
<link href="https://fonts.googleapis.com/css2?family=Anton&family=Archivo+Black&family=Encode+Sans+Semi+Condensed:wght@500&display=swap" rel="stylesheet">
<style>
  :root {
    --navy: #0b1a4b;
    --title-blue: #2b3f98;
    --panel-blue: #0399d5;
    --white: #ffffff;
    --star-light: #fff34a;
    --star-mid: #f4e21c;
    --star-dark: #c9b400;
  }
  html, body {
    margin: 0;
    padding: 0;
    overflow: hidden;
    background: var(--navy);
  }
  .cover {
    position: relative;
    width: 818px;
    height: 1200px;
    background: var(--navy);
    overflow: hidden;
  }
  .cover-art {
    position: absolute;
    inset: 0;
    width: 818px;
    height: 1200px;
    display: block;
  }
  .title-text {
    font-family: "Anton", "Impact", sans-serif;
    fill: var(--title-blue);
    stroke: var(--white);
    stroke-width: 3;
    paint-order: stroke;
  }
  .subtitle-text {
    font-family: "Encode Sans Semi Condensed", "Arial Narrow", sans-serif;
    font-weight: 500;
    font-size: 44px;
    fill: var(--white);
  }
  .author-text {
    font-family: "Archivo Black", "Arial Black", sans-serif;
    font-size: 36px;
    fill: var(--title-blue);
    stroke: var(--white);
    stroke-width: 2;
    paint-order: stroke;
  }
</style>
</head>
<body>
<main class="cover">
  <svg class="cover-art" viewBox="0 0 818 1200" xmlns="http://www.w3.org/2000/svg">
    <defs>
      <filter id="title-glow" x="-10%" y="-20%" width="120%" height="140%">
        <feGaussianBlur in="SourceAlpha" stdDeviation="5" result="blur"/>
        <feFlood flood-color="#ffffff" flood-opacity="0.55"/>
        <feComposite in2="blur" operator="in" result="glow"/>
        <feMerge><feMergeNode in="glow"/><feMergeNode in="SourceGraphic"/></feMerge>
      </filter>
      <filter id="star-shadow" x="-20%" y="-20%" width="150%" height="150%">
        <feDropShadow dx="6" dy="8" stdDeviation="5" flood-color="#000000" flood-opacity="0.6"/>
      </filter>
      <radialGradient id="star-fill" cx="45%" cy="45%" r="65%">
        <stop offset="0%" stop-color="var(--star-light)"/>
        <stop offset="60%" stop-color="var(--star-mid)"/>
        <stop offset="100%" stop-color="var(--star-dark)"/>
      </radialGradient>
      <polygon id="star" points="0,-84 19.8,-27.2 80,-26 32,10.4 49.4,68 0,33.6 -49.4,68 -32,10.4 -80,-26 -19.8,-27.2"/>
    </defs>

    <g class="title" filter="url(#title-glow)">
      <text class="title-text" x="80" y="176" textLength="650" lengthAdjust="spacingAndGlyphs"><tspan font-size="176">S</tspan><tspan font-size="132">TANDING</tspan></text>
      <text class="title-text" x="110" y="323" textLength="600" lengthAdjust="spacingAndGlyphs"><tspan font-size="176">G</tspan><tspan font-size="132">ROWTH</tspan></text>
    </g>

    <g class="rating-stars" fill="url(#star-fill)" stroke="#fffbd0" stroke-width="1.5" filter="url(#star-shadow)">
      <use href="#star" x="90" y="497"/>
      <use href="#star" x="250" y="497"/>
      <use href="#star" x="409" y="497"/>
      <use href="#star" x="569" y="497"/>
      <use href="#star" x="728" y="497"/>
    </g>

    <polygon class="subtitle-panel" points="8,661 810,661 810,1186 8,838" fill="var(--panel-blue)"/>

    <g class="subtitle">
      <text class="subtitle-text" x="418" y="714" text-anchor="middle">Keys to Glowing Customer Ratings</text>
      <text class="subtitle-text" x="418" y="779" text-anchor="middle">That Fill The Calendar</text>
      <text class="subtitle-text" x="418" y="844" text-anchor="middle" textLength="700" lengthAdjust="spacingAndGlyphs">and Draw Fresh Clients Through Every Entrance!</text>
    </g>

    <text class="author-text" x="10" y="1176" textLength="448" lengthAdjust="spacingAndGlyphs">Fireman Dale Orsworth</text>
  </svg>
</main>
</body>
</html>
```